Nordisk Bygnad needs a membership brochure

Nordisk Bygnad is a business association for the Fjordland Joinery Guild ,(our members produce e.g doors, windows, stairs and furniture). We represent 325 businesses, 6500 employees and an annual 1 billion Euro turnover. We need a brochure to attract new members/ customers, but we also need to show existing members what we can offer and what we work for. Our work is political and environmental. We offer legal help, we provide insurance and other member benefits.

Our logo and design manual is 3 years old, and we want the brochure to be founded on our existing colors, which can be found on our website. (www.bygnad.no)

I will provide/write the text for the brochure, as it will be in Norwegian.
To give you some idea, the headlines will be:

What is Nordisk Bygnad?
Legal help
Insurance
HMS
Statistics
Technology
Local branches
Activities:
- Craft Academy
- Timber Fair
- Trade Assembly
- Annual meeting

Target Market(s)

Managers in the Wood Manufacturing industry in Norway

Industry/Entity Type

Political

Font styles to use
Sans Serif
Other font styles liked:
• Arial

Requirements
Must have
• The brochure should have 8 pages. The brochure must be based on our design manual (Profilveileder is uploaded) and our website www.bygnad.no, regarding to colors and fonts.

Use the guidelines "freely".

Nice to have
• It would be nice with some new pictures, but if pictures are needed, i can provide a lot!

```html
<!DOCTYPE html>
<html lang="no">
<head>
<meta charset="utf-8">
<title>Nordisk Bygnad – Kvalitet, Teknologi, HMS</title>
<link rel="stylesheet" href="https://fonts.googleapis.com/css2?family=Arimo:wght@400;700&display=swap">
<style>
  :root {
    --wood-beige: #f0d99c;
    --bark-brown: #4b3327;
    --leaf-green: #77973a;
    --ink: #111111;
    --frame-white: #ffffff;
    --photo-light: #d9c7ae;
    --photo-mid: #a48366;
    --photo-dark: #5e4a3c;
  }
  * { margin: 0; padding: 0; box-sizing: border-box; }
  html, body {
    width: 1200px;
    height: 848px;
    overflow: hidden;
    background: #ffffff;
  }
  .page {
    position: relative;
    width: 1200px;
    height: 848px;
    overflow: hidden;
    background: var(--wood-beige);
    font-family: "Arimo", Arial, sans-serif;
    color: var(--ink);
  }
  .corner { position: absolute; inset: 0; width: 1200px; height: 848px; }
  .corner polygon { fill: var(--bark-brown); }

  .section-title {
    position: absolute;
    font-weight: 700;
    font-size: 55px;
    line-height: 1;
    color: var(--leaf-green);
    letter-spacing: 0.2px;
  }
  .body-text {
    position: absolute;
    font-size: 17.6px;
    line-height: 27px;
    white-space: nowrap;
  }

  .title-quality { left: 175px; top: 88px; }
  .quality-lead { left: 175px; top: 140px; }
  .quality-lead .hang { margin-left: 0; }
  .quality-tail { left: 658px; top: 221px; }

  .workshop-photo {
    position: absolute;
    left: 0;
    top: 259px;
    width: 633px;
    height: 289px;
    background:
      radial-gradient(ellipse at 30% 35%, var(--photo-light) 0%, transparent 55%),
      linear-gradient(100deg, var(--photo-dark) 0%, var(--photo-mid) 35%, var(--photo-light) 70%, var(--photo-mid) 100%);
  }
  .photo-frame {
    position: absolute;
    left: 0;
    top: 0;
    width: 1200px;
    height: 848px;
    pointer-events: none;
  }
  .photo-frame polygon {
    fill: none;
    stroke: var(--frame-white);
    stroke-width: 4.5;
  }

  .title-technology { left: 655px; top: 323px; }
  .technology-text { left: 658px; top: 374px; }

  .title-hms { left: 655px; top: 498px; }
  .hms-lead { left: 658px; top: 552px; }
  .hms-tail { left: 176px; top: 579px; }
</style>
</head>
<body>
<main class="page">
  <svg class="corner" viewBox="0 0 1200 848" aria-hidden="true">
    <polygon points="1075,0 1200,0 1200,58"/>
    <polygon points="0,712 0,848 186,848"/>
  </svg>

  <h2 class="section-title title-quality">Kvalitet</h2>
  <p class="body-text quality-lead">
    Nordisk Bygnad jobber for bedreoffentlig tilsyn og produktkontroll. Vi er opptatt av at norske kunder og forbrukere<br>
    skal være trygge på kvaliteten på de produktene de kjøper, og at de blir gitt korrekt og tilstrekkelig informasjon.<br>
    Nordisk Bygnad skal være en aktiv pådriver for medlemmenes interesser i utviklingen av nye forskrifter. Vi tilbyr
  </p>
  <p class="body-text quality-tail">
    et svært prisgunstig kvalitetssystem til medlemmene<br>
    våre som er spesielt oppbygd for trevareindustrien.
  </p>

  <div class="workshop-photo" role="img" aria-label="Fotografi av en snekker med vernebriller som måler en treplate i verkstedet"></div>
  <svg class="photo-frame" viewBox="0 0 1200 848" aria-hidden="true">
    <polygon points="174,254 392,254 441,292 441,550 222,550 174,496"/>
  </svg>

  <h2 class="section-title title-technology">Teknologi</h2>
  <p class="body-text technology-text">
    Den teknologiske utviklingen er i rivende utvikling. Som<br>
    bransjeforening skal vi ligge i forkant. Vi skal videreformidle<br>
    relevant informasjon og kompetanse.
  </p>

  <h2 class="section-title title-hms">HMS</h2>
  <p class="body-text hms-lead">
    Systematisk HMS arbeid gir fornøyde ansatte som bidrar til
  </p>
  <p class="body-text hms-tail">
    fornøyde kunder. Vi tilbyr lovpålagt HMS kurs svært prisgunstig for våre medlemmer. Vi tilbyr også tilpasset HMS<br>
    gjennomgang i bedriften. Dette kan være nyttig før Arbeidskontrollen kommer, eller dersom du allerede har hatt tilsyn,<br>
    kan vi hjelpe deg med hvordan du best løser pålegg.
  </p>
</main>
</body>
</html>
```